New business card design needed for Trucking/Staffing company!

I am looking for a business card design. The business name is Harbor Lane Freightworks, LLC. This company is a staffing company for commercial drivers/truck drivers. Most of our customers are trucking/supply companies. Our colors are blue/black/white/grey. The info I have on my current business cards is
-Spot for a name
-2 lines for an address
-3 lines for Office, cell, and fax
-email
-website(currently on backside of card with logo but can go anywhere)
Updates

Project Deadline Extended
Reason: Open to more designs

Target Market(s)

Trucking companies, building supply companies

Industry/Entity Type

Business

Contact Information for Business Card

Edgy but professional

Font styles to use
Other font styles liked:
• Open to suggestions

Colors
0555a3
000000
ffffff
9d9d9d

Requirements
Must have
• Must have the logo incorporated

```html
<!DOCTYPE html>
<html lang="en">
<head>
<meta charset="utf-8">
<title>Harbor Lane Freightworks, LLC – Business Card</title>
<link rel="stylesheet" href="https://fonts.googleapis.com/css2?family=Michroma&family=Roboto:wght@400&display=swap">
<style>
  :root {
    --brand-blue: #0d1fe6;
    --ink: #000000;
    --paper: #ffffff;
    --stage: #dcdcdc;
    --rule: #e6e6e6;
  }
  * { margin: 0; padding: 0; box-sizing: border-box; }
  html, body { width: 1189px; height: 1200px; overflow: hidden; }
  body { background: var(--stage); position: relative; font-family: "Roboto", Arial, sans-serif; }

  .card { position: absolute; left: 124px; width: 940px; height: 530px; overflow: hidden; }
  .card--front { top: 55px; background: var(--ink); color: var(--paper); }
  .card--back { top: 615px; background: var(--paper); }

  .brand-name { font-family: "Michroma", sans-serif; font-weight: 400; color: var(--brand-blue); line-height: 1.25; }
  .brand { position: absolute; display: flex; align-items: center; }
  .brand__mark { background: var(--brand-blue); flex: none; }

  .card--front .brand { left: 34px; top: 240px; width: 390px; gap: 14px; }
  .card--front .brand__mark { width: 20px; height: 20px; }
  .card--front .brand-name { font-size: 21px; }

  .divider { position: absolute; left: 448px; top: 43px; width: 2px; height: 447px; background: var(--rule); }

  .person { position: absolute; left: 462px; top: 68px; }
  .person__name { font-family: "Michroma", sans-serif; font-size: 27px; color: var(--brand-blue); letter-spacing: 0.5px; text-transform: uppercase; }
  .person__role { font-family: "Michroma", sans-serif; font-size: 18px; color: var(--paper); margin-top: 6px; text-transform: uppercase; }

  .contact { position: absolute; left: 462px; top: 282px; list-style: none; }
  .contact__item { display: flex; align-items: flex-start; font-size: 25px; line-height: 32px; height: 32px; margin-bottom: 1px; }
  .contact__item--address { height: auto; line-height: 28px; margin-top: 4px; }
  .contact__icon { width: 16px; height: 16px; margin-top: 7px; margin-right: 22px; flex: none; }

  .card--back .brand { left: 0; right: 0; top: 170px; justify-content: center; gap: 22px; }
  .card--back .brand__mark { width: 38px; height: 38px; }
  .card--back .brand-name { font-size: 40px; text-align: left; }

  .web-band { position: absolute; left: 0; right: 0; bottom: 0; height: 68px; background: var(--brand-blue); color: var(--paper); font-size: 38px; display: flex; align-items: center; justify-content: center; }
</style>
</head>
<body>
  <section class="card card--front" aria-label="Business card front">
    <div class="brand">
      <span class="brand__mark"></span>
      <span class="brand-name">Harbor Lane<br>Freightworks, LLC</span>
    </div>
    <div class="divider"></div>
    <div class="person">
      <p class="person__name">Marla Dennison</p>
      <p class="person__role">Owner</p>
    </div>
    <ul class="contact">
      <li class="contact__item">
        <svg class="contact__icon" viewBox="0 0 16 16" aria-hidden="true"><rect width="16" height="16" fill="var(--brand-blue)"/><path d="M5 3.5l2 2-1 1.2c.6 1.4 1.8 2.6 3.2 3.2l1.2-1 2 2-1.2 1.6C7.5 12 4 8.5 3.5 4.7z" fill="#fff"/></svg>
        555 214 0831
      </li>
      <li class="contact__item">
        <svg class="contact__icon" viewBox="0 0 16 16" aria-hidden="true"><rect width="16" height="16" fill="var(--brand-blue)"/><path d="M3 6c2-2.5 8-2.5 10 0v1.5h-2.5V6.3h-5v1.2H3zM4.5 8.5h7v4h-7z" fill="#fff"/></svg>
        555 214 0832
      </li>
      <li class="contact__item">
        <svg class="contact__icon" viewBox="0 0 16 16" aria-hidden="true"><rect width="16" height="16" fill="var(--brand-blue)"/><path d="M5 3h6v3H5zM3 7h10v5H3z" fill="#fff"/><rect x="5" y="9" width="6" height="4" fill="var(--brand-blue)"/></svg>
        555 214 0833
      </li>
      <li class="contact__item">
        <svg class="contact__icon" viewBox="0 0 16 16" aria-hidden="true"><rect width="16" height="16" fill="var(--brand-blue)"/><rect x="3" y="5" width="10" height="7" fill="#fff"/><path d="M3 5l5 4 5-4" fill="none" stroke="var(--brand-blue)" stroke-width="1"/></svg>
        mdennison@harborlanefw.com
      </li>
      <li class="contact__item">
        <svg class="contact__icon" viewBox="0 0 16 16" aria-hidden="true"><rect width="16" height="16" fill="var(--brand-blue)"/><circle cx="8" cy="8" r="4.5" fill="none" stroke="#fff" stroke-width="1.2"/><path d="M3.5 8h9M8 3.5c-2 2.5-2 6.5 0 9M8 3.5c2 2.5 2 6.5 0 9" fill="none" stroke="#fff" stroke-width="1"/></svg>
        harborlanefw.com
      </li>
      <li class="contact__item contact__item--address">
        <svg class="contact__icon" viewBox="0 0 16 16" aria-hidden="true"><rect width="16" height="16" fill="var(--brand-blue)"/><path d="M8 13.5S4.5 9.5 4.5 7a3.5 3.5 0 017 0c0 2.5-3.5 6.5-3.5 6.5z" fill="#fff"/><circle cx="8" cy="7" r="1.3" fill="var(--brand-blue)"/></svg>
        <span>1470 Quayside Ct #210<br>&nbsp;Bay Ridge FL 34600</span>
      </li>
    </ul>
  </section>

  <section class="card card--back" aria-label="Business card back">
    <div class="brand">
      <span class="brand__mark"></span>
      <span class="brand-name">Harbor Lane<br>Freightworks, LLC</span>
    </div>
    <div class="web-band">www .harborlanefw.com</div>
  </section>
</body>
</html>
```